Business Card Professional Clean - Ledgerpeak

Create a business card for my company that deals with Cryptocurrencies. I have a few designs ideas that I'd like to be implemented. Thanks! I will include the logo files, and a link to the design styles that I like.

Target Market(s)

Professionals

Industry/Entity Type

Consulting

Contact Information for Business Card

Name: Mark Dunn
Title: CEO/Technical Director
Phone: (587)430-9158
E-mail: mdunn@ledgerpeak.example
Address: Suite 512, 208-3375 Harwood Lane NW

Twitter: @LedgerPeakYYC
Instagram: ledgerpeakyyc

Colors
92b5d7
3276b5
33a6d7
85acd3
85cae6
0592cd

Requirements
Must have
• Some colors that match with the logo and the pictures I put in below.
• Ideally the finished product would look something like the attachments showing the color gradient I want.
Nice to have
• Please see some of the attachments I've included. This is very close to the final product that I would like to see. If someone could recreate something like those I would definitely feel pretty good about it.
• For the instagram and twitter please use the symbols/icon to represent it on the card.
Should not have
• No crazy colors and unprofessional styles. I just want clear info. Don't go outside the boundaries of the colors in the attachment and we should be good. No crazy weird fonts either.

```html
<!DOCTYPE html>
<html lang="en">
<head>
<meta charset="utf-8">
<title>Ledgerpeak Business Card</title>
<link href="https://fonts.googleapis.com/css2?family=Ubuntu:wght@500&family=Open+Sans:wght@300;400&display=swap" rel="stylesheet">
<style>
  :root {
    --backdrop: #1c1c1e;
    --card-top: #414144;
    --card-bottom: #2b2b2e;
    --tile-light: #5a5a5e;
    --tile-dark: #333336;
    --text-light: #e6e6e8;
    --accent-blue: #33a6d7;
    --accent-deep: #0592cd;
  }
  * { box-sizing: border-box; margin: 0; padding: 0; }
  html, body { width: 1200px; height: 896px; overflow: hidden; }
  body {
    background: var(--backdrop);
    font-family: "Open Sans", Arial, sans-serif;
    position: relative;
  }
  .card {
    position: absolute;
    top: 293px;
    width: 540px;
    height: 309px;
    border-radius: 18px;
    overflow: hidden;
    background: linear-gradient(160deg, var(--card-top), var(--card-bottom));
    box-shadow: 0 14px 30px rgba(0,0,0,.55);
  }
  .card--front { left: 40px; }
  .card--back { left: 620px; }
  .tile-band {
    position: absolute;
    left: 0; right: 0;
    height: 92px;
  }
  .tile-band--top {
    top: 0;
    background: linear-gradient(180deg, var(--tile-dark) 0%, rgba(90,90,94,.55) 55%, rgba(65,65,68,0) 100%);
  }
  .tile-band--bottom {
    bottom: 0;
    background: linear-gradient(0deg, var(--tile-light) 0%, rgba(80,80,84,.5) 50%, rgba(50,50,53,0) 100%);
  }
  .brand {
    position: absolute;
    inset: 0;
    display: flex;
    align-items: center;
    justify-content: center;
  }
  .brand__name {
    font-family: "Open Sans", Arial, sans-serif;
    font-weight: 300;
    font-size: 40px;
    letter-spacing: 2px;
    color: var(--text-light);
  }
  .person {
    position: absolute;
    left: 52px;
    top: 118px;
    color: var(--text-light);
  }
  .person__name {
    font-family: "Ubuntu", Arial, sans-serif;
    font-weight: 500;
    font-size: 34px;
    color: var(--accent-blue);
    line-height: 1;
  }
  .person__title {
    font-weight: 300;
    font-size: 15px;
    margin-top: 6px;
    margin-bottom: 8px;
  }
  .contact-line {
    display: flex;
    align-items: center;
    gap: 8px;
    font-weight: 300;
    font-size: 14px;
    line-height: 21px;
  }
  .contact-line svg { width: 12px; height: 12px; flex: none; }
  .details {
    position: absolute;
    right: 40px;
    top: 112px;
    color: var(--text-light);
  }
  .social-dot {
    width: 10px; height: 10px;
    border-radius: 50%;
    background: var(--accent-deep);
    flex: none;
  }
  .address {
    margin-top: 6px;
    font-weight: 300;
    font-size: 14px;
    line-height: 20px;
  }
</style>
</head>
<body>
  <section class="card card--front" aria-label="Card front">
    <div class="tile-band tile-band--top" role="img" aria-label="Grey checker tile pattern fading down"></div>
    <div class="tile-band tile-band--bottom" role="img" aria-label="Grey checker tile pattern fading up"></div>
    <div class="brand">
      <span class="brand__name">Ledgerpeak</span>
    </div>
  </section>

  <section class="card card--back" aria-label="Card back">
    <div class="tile-band tile-band--top" role="img" aria-label="Grey checker tile pattern fading down"></div>
    <div class="tile-band tile-band--bottom" role="img" aria-label="Grey checker tile pattern fading up"></div>

    <div class="person">
      <p class="person__name">Mark Dunn</p>
      <p class="person__title">CEO/Technical Director</p>
      <p class="contact-line">
        <svg viewBox="0 0 12 12" aria-hidden="true"><path d="M3 1 L5 3.5 L4 5 Q5.5 7.5 7 8 L8.5 7 L11 9 L9.5 11 Q4 10.5 1 3 Z" fill="none" stroke="#33a6d7" stroke-width="1.1"/></svg>
        (587)430-9158
      </p>
      <p class="contact-line">
        <svg viewBox="0 0 12 12" aria-hidden="true"><rect x="1" y="2.5" width="10" height="7" fill="none" stroke="#33a6d7" stroke-width="1.1"/><path d="M1 2.5 L6 6.5 L11 2.5" fill="none" stroke="#33a6d7" stroke-width="1.1"/></svg>
        mdunn@ledgerpeak.example
      </p>
    </div>

    <div class="details">
      <p class="contact-line"><span class="social-dot"></span>@LedgerPeakYYC</p>
      <p class="contact-line"><span class="social-dot"></span>ledgerpeakyyc</p>
      <p class="address">Suite 512, 208-3375<br>Harwood Lane NW</p>
    </div>
  </section>
</body>
</html>
```